Lantern Hollow Distillery Rum Label Project

We are a new distillery opening up in the old train station in Mount Holly, NJ. We will be making rum, gin, and vodka in the first year of operation, and hope to expand to other products in the future. We need label designs for our brand "Lantern Hollow Rum TM" that complies with QFR regulations including items such as UPC, surgeon general warning, font size requirement, volume, proof, ect. For further information regarding the labeling requirements for all the legal stuff: https://www.qfrexample.org/liquor/kpm/section1.pdf
Updates

We will also need a tamper evident seal. Simple is fine.

Target Market(s)

25-35 casual cocktail drinkers, 35-65 craft spirit enthusiasts, all legal ages local craft market celebrants

Font styles to use
Serif
Sans Serif
Decorative

Colors

Designer to choose colors to be used in the design.

Requirements
Must have
• Must adhere to QFR guidelines https://www.qfrexample.org/liquor/kpm/section1.pdf
• Gold foiling-- don't bleed with foil to prevent foil edges from curling
Nice to have
• References to Mount Holly, 1800s, trains, signage, maps, tickets, history, motto: "All Aboard!"
Should not have
• References to "getting wrecked". The brand is more tongue in cheek and playful.

```html
<!DOCTYPE html>
<html lang="en">
<head>
<meta charset="utf-8">
<title>Lantern Hollow Distillery – Rum Label and Seal</title>
<link href="https://fonts.googleapis.com/css2?family=Righteous&family=Oswald:wght@300;400;600&family=Courier+Prime:wght@400;700&display=swap" rel="stylesheet">
<style>
  :root {
    --ink: #1b1b1b;
    --paper: #ffffff;
    --gold-dark: #b4842a;
    --gold-light: #f4d67e;
    --gold-mid: #d3a443;
  }
  html, body { margin: 0; padding: 0; overflow: hidden; background: var(--paper); }
  .canvas { position: relative; width: 1200px; height: 1106px; background: var(--paper); overflow: hidden; color: var(--ink); }
  .ticket-outline { position: absolute; left: 98px; top: 334px; }
  .label-frame { position: absolute; left: 128px; top: 372px; width: 340px; height: 596px; box-sizing: border-box; border: 2px solid var(--ink); }
  .dots { position: absolute; border-top: 3px dotted var(--ink); height: 0; }
  .brand-row { position: absolute; left: 128px; top: 425px; width: 340px; display: flex; justify-content: center; }
  .brand-mark { display: inline-flex; align-items: center; gap: 6px; padding: 0 8px; background: var(--paper);
    font-family: "Oswald", sans-serif; font-weight: 600; font-size: 15px; line-height: 20px; letter-spacing: 1px; }
  .brand-mark .dot-badge { width: 12px; height: 12px; border-radius: 50%; background: var(--ink); }
  .headline { position: absolute; left: 128px; width: 340px; top: 486px; text-align: center; font-family: "Righteous", sans-serif; font-size: 31px; letter-spacing: 0.5px; line-height: 1; }
  .subhead { position: absolute; left: 128px; width: 340px; top: 538px; display: flex; align-items: center; justify-content: center; gap: 8px;
    font-family: "Oswald", sans-serif; font-weight: 400; font-size: 28px; letter-spacing: 1px; line-height: 1; }
  .subhead .rule { flex: 0 0 74px; border-top: 3px dotted var(--ink); }
  .product { position: absolute; left: 128px; width: 340px; top: 572px; text-align: center; font-family: "Righteous", sans-serif; font-size: 132px; line-height: 1; letter-spacing: 2px; }
  .motto-band { position: absolute; left: 128px; top: 709px; width: 340px; height: 44px; display: flex; align-items: center; justify-content: center;
    background: linear-gradient(90deg, var(--gold-dark), var(--gold-light) 45%, var(--gold-mid) 75%, var(--gold-dark));
    font-family: "Courier Prime", monospace; font-weight: 700; font-size: 22px; letter-spacing: 4px; }
  .copy { position: absolute; left: 128px; width: 340px; text-align: center; font-family: "Oswald", sans-serif; font-weight: 300; font-size: 16px; line-height: 22px; letter-spacing: 0.6px; text-transform: uppercase; }
  .spec-table { position: absolute; left: 150px; top: 846px; width: 298px; height: 60px; border-collapse: collapse; font-family: "Courier Prime", monospace; }
  .spec-table td { border: 2px solid var(--ink); text-align: center; vertical-align: top; padding: 2px 0 0; }
  .spec-table .key { display: block; font-size: 14px; letter-spacing: 1px; }
  .spec-table .val { display: block; font-size: 28px; line-height: 28px; letter-spacing: 3px; }
  .seal { position: absolute; left: 530px; top: 340px; }
  .seal text { font-family: "Oswald", sans-serif; fill: var(--ink); }
</style>
</head>
<body>
<div class="canvas">

  <svg class="ticket-outline" width="400" height="674" viewBox="-1 -1 402 676" aria-hidden="true">
    <path fill="var(--paper)" stroke="var(--ink)" stroke-width="1.5"
      d="M0,24 A24,24 0 0 0 24,0
         H47 A9,9 0 0 0 65,0 H79 A9,9 0 0 0 97,0 H111 A9,9 0 0 0 129,0 H143 A9,9 0 0 0 161,0 H175 A9,9 0 0 0 193,0
         H207 A9,9 0 0 0 225,0 H239 A9,9 0 0 0 257,0 H271 A9,9 0 0 0 289,0 H303 A9,9 0 0 0 321,0 H335 A9,9 0 0 0 353,0
         H376 A24,24 0 0 0 400,24 V650 A24,24 0 0 0 376,674
         H353 A9,9 0 0 0 335,674 H321 A9,9 0 0 0 303,674 H289 A9,9 0 0 0 271,674 H257 A9,9 0 0 0 239,674 H225 A9,9 0 0 0 207,674
         H193 A9,9 0 0 0 175,674 H161 A9,9 0 0 0 143,674 H129 A9,9 0 0 0 111,674 H97 A9,9 0 0 0 79,674 H65 A9,9 0 0 0 47,674
         H24 A24,24 0 0 0 0,650 Z"/>
  </svg>

  <div class="label-frame"></div>

  <div class="dots" style="left:146px; top:437px; width:304px;"></div>
  <div class="brand-row"><span class="brand-mark"><span class="dot-badge"></span><span>LANTERN HOLLOW</span></span></div>

  <div class="headline">LANTERN HOLLOW</div>
  <div class="subhead"><span class="rule"></span><span>DISTILLERY</span><span class="rule"></span></div>
  <div class="product">RUM</div>

  <div class="motto-band">ALL ABOARD!</div>

  <div class="copy" style="top:766px;">Lorem ipsum dolor sit amet contetur<br>adipiscing elit, sed do eiusmod temporo<br>incididunt ut labore et dolore magnanis</div>

  <div class="dots" style="left:148px; top:837px; width:302px;"></div>
  <table class="spec-table">
    <tr>
      <td style="width:74px;"><span class="key">VOL.</span><span class="val">250</span></td>
      <td style="width:150px;"><span class="key">BTL.NO./BATCH</span><span class="val">07</span></td>
      <td><span class="key">BOTTLE</span><span class="val">84</span></td>
    </tr>
  </table>
  <div class="dots" style="left:148px; top:912px; width:302px;"></div>
  <div class="copy" style="top:927px;">Lorem ipsum dolor sit amet contetur</div>

  <svg class="seal" width="170" height="620" viewBox="0 0 170 620" role="img" aria-label="Tamper evident neck seal, gold foil strip">
    <defs>
      <linearGradient id="foil" x1="0" y1="0" x2="0" y2="1">
        <stop offset="0" stop-color="var(--gold-dark)"/>
        <stop offset="0.25" stop-color="var(--gold-light)"/>
        <stop offset="0.5" stop-color="var(--gold-mid)"/>
        <stop offset="0.75" stop-color="var(--gold-light)"/>
        <stop offset="1" stop-color="var(--gold-dark)"/>
      </linearGradient>
    </defs>
    <rect x="52" y="6" width="66" height="608" fill="var(--paper)" stroke="#555" stroke-width="1"/>
    <rect x="57" y="11" width="56" height="598" fill="url(#foil)"/>
    <circle cx="86" cy="318" r="76" fill="var(--paper)" stroke="var(--ink)" stroke-width="1.5"/>
    <circle cx="86" cy="318" r="64" fill="none" stroke="var(--ink)" stroke-width="14"/>
    <rect x="62" y="190" width="48" height="256" fill="var(--paper)" stroke="var(--ink)" stroke-width="3"/>
    <text x="86" y="318" transform="rotate(-90 86 318)" text-anchor="middle" dominant-baseline="central" font-size="24" font-weight="600" letter-spacing="1" textLength="226" lengthAdjust="spacingAndGlyphs">LANTERN HOLLOW</text>
    <text x="86" y="32" transform="rotate(180 86 32)" text-anchor="middle" dominant-baseline="central" font-size="20" letter-spacing="2">RUM</text>
    <text x="86" y="118" transform="rotate(90 86 118)" text-anchor="middle" dominant-baseline="central" font-size="19" letter-spacing="1" textLength="116" lengthAdjust="spacingAndGlyphs">HAND CRAFTED</text>
    <text x="86" y="510" transform="rotate(-90 86 510)" text-anchor="middle" dominant-baseline="central" font-size="19" letter-spacing="1" textLength="116" lengthAdjust="spacingAndGlyphs">HAND CRAFTED</text>
    <text x="86" y="592" text-anchor="middle" dominant-baseline="central" font-size="20" letter-spacing="2">RUM</text>
  </svg>

</div>
</body>
</html>
```